Employee Benefits and Insurance Consulting

We are an existing company with over 30 years experience but are changing our name. We would like a simple design with grey tones.

Industry/Entity Type

Insurance

Contact Information for Business Card

Marlow Benefits Consulting
Gerald P Odell CEO
5172 Brackenfield Road
Fernbrook, TN 37794
gerald@marlowbx.com
865-412-3396 - O
865-247-5081 - C

```html
<!DOCTYPE html>
<html lang="en">
<head>
<meta charset="utf-8">
<title>Marlow Benefits Consulting – Business Card</title>
<link rel="stylesheet" href="https://fonts.googleapis.com/css2?family=Nunito+Sans:wght@700;800;900&display=swap">
<style>
  :root {
    --card-bg: #e7e5e6;
    --ink: #111111;
    --wave-mid: #7a7a7a;
    --wave-light: #8d8d8d;
    --wave-dark: #414141;
    --mark-fill: #5e5e5e;
  }
  html, body {
    margin: 0;
    padding: 0;
    overflow: hidden;
    background: #ffffff;
  }
  .card {
    position: relative;
    width: 1200px;
    height: 688px;
    background: var(--card-bg);
    overflow: hidden;
    font-family: "Nunito Sans", Arial, sans-serif;
    color: var(--ink);
  }
  .waves {
    position: absolute;
    inset: 0;
    width: 1200px;
    height: 688px;
  }
  .brand-mark {
    position: absolute;
    left: 26px;
    top: 30px;
    width: 100px;
    height: 100px;
    background: var(--mark-fill);
  }
  .company-name {
    position: absolute;
    left: 158px;
    top: 18px;
    margin: 0;
    font-size: 51px;
    font-weight: 800;
    line-height: 66px;
    letter-spacing: 0.2px;
  }
  .rule {
    position: absolute;
    width: 400px;
    height: 12px;
  }
  .rule--top { left: 150px; top: 166px; }
  .rule--bottom { left: 155px; top: 268px; }
  .person {
    position: absolute;
    left: 150px;
    top: 192px;
    font-size: 28px;
    font-weight: 800;
    line-height: 38px;
  }
  .person__title {
    display: block;
    padding-left: 104px;
  }
  .address {
    position: absolute;
    top: 312px;
    font-size: 26px;
    font-weight: 800;
    line-height: 34px;
    padding-left: 22px;
  }
  .address::before {
    content: "";
    position: absolute;
    left: 0;
    top: 15px;
    width: 9px;
    height: 9px;
    border-radius: 50%;
    background: var(--ink);
  }
  .address--street { left: 152px; }
  .address--city { left: 534px; }
  .phones {
    position: absolute;
    left: 151px;
    top: 410px;
    display: flex;
    align-items: center;
    gap: 19px;
  }
  .phones__numbers {
    font-size: 25px;
    font-weight: 800;
    line-height: 32px;
  }
  .phone-icon { width: 34px; height: 56px; }
  .email {
    position: absolute;
    left: 148px;
    top: 492px;
    display: flex;
    align-items: center;
    gap: 14px;
    font-size: 22px;
    font-weight: 800;
  }
  .mail-icon { width: 46px; height: 24px; }
</style>
</head>
<body>
  <div class="card">
    <svg class="waves" viewBox="0 0 736 422" preserveAspectRatio="none" aria-hidden="true">
      <path fill="var(--wave-mid)" d="M0 262 C130 200 330 215 470 300 C560 350 690 300 736 170 L736 422 L0 422 Z"/>
      <path fill="var(--wave-light)" d="M420 422 C520 380 640 360 700 300 C720 280 730 240 736 215 L736 422 Z"/>
      <path fill="var(--wave-dark)" d="M170 422 C330 385 560 370 660 330 C700 312 725 290 736 270 L736 422 Z"/>
    </svg>

    <div class="brand-mark" aria-hidden="true"></div>
    <h1 class="company-name">Marlow Benefits<br>Consulting</h1>

    <svg class="rule rule--top" viewBox="0 0 400 12" preserveAspectRatio="none" aria-hidden="true">
      <path d="M0 2 L400 6 L0 12 Z" fill="var(--ink)"/>
    </svg>
    <div class="person">
      <span class="person__name">Gerald P Odell</span>
      <span class="person__title">CEO</span>
    </div>
    <svg class="rule rule--bottom" viewBox="0 0 400 12" preserveAspectRatio="none" aria-hidden="true">
      <path d="M0 2 L400 6 L0 12 Z" fill="var(--ink)"/>
    </svg>

    <div class="address address--street">5172 Brackenfield Road</div>
    <div class="address address--city">Fernbrook, TN 37794</div>

    <div class="phones">
      <svg class="phone-icon" viewBox="0 0 34 56" aria-hidden="true">
        <rect x="2" y="2" width="30" height="52" rx="4" fill="var(--ink)"/>
        <rect x="7" y="8" width="20" height="36" fill="#ffffff"/>
      </svg>
      <div class="phones__numbers">
        <div>865-412-3396</div>
        <div>865-247-5081</div>
      </div>
    </div>

    <div class="email">
      <svg class="mail-icon" viewBox="0 0 46 24" aria-hidden="true">
        <rect x="1" y="1" width="44" height="22" fill="var(--ink)"/>
        <path d="M1 1 L23 14 L45 1" fill="none" stroke="var(--card-bg)" stroke-width="2"/>
      </svg>
      <span>gerald@marlowbx.com</span>
    </div>
  </div>
</body>
</html>
```